Flyer für den Bereich Solarenergie
Zielgruppe
Guten Tag,
wir sind im Bereich Solarenergie tätig. Wir suchen nun Hallen mit großen Dächern, die wir anmieten können, um darauf Solaranlagen zu bauen. Wir machen dabei alles aus einer Hand. der Eigentümer muss nichts machen. Er bekommt sogar Geld von uns und das Dach ist sowieso meistens leer.
Aufgabenstellung
Wir möchten einen DINA4 Flyer den wir als PDF in Emails verschicken können. Farbdaten sollten Sie aus den Logodateien im Anhang entnehmen können. Richten Sie sich auch gerne an das Design des Logos und der Website. Dabei sollen kurz die wichtigsten Key Faktoren aufgelistet werden und das Unternehmen kurz dargestellt werden. Hier einmal die Texte:
Beschreibung zum Unternehmen:
Veltrano ist Experte für grüne Energietechnik mit über 20 Jahren Erfahrung. Mit über 1.000 zufriedenen Kunden im Bereich Photovoltaikanlagen können wir auf einen großen Erfahrungsschatz zurückgreifen. Wenn wir am Werk sind, wird nicht nur das Klima geschont, sondern auch Sie als Kunde profitieren. Mit uns wird nachhaltiges Handeln kinderleicht und gleichzeitig rentabel.
Erwirtschaften auch Sie mit Ihrem Dach nun bares Geld!
Ihre Vorteile:
- Umwelt schonen durch das Produzieren von grünem Strom
- Dach schützen vor Emissionen
- Dachsanierungen anstatt von Mietzahlungen möglich
- Keine Kosten, da wir alle Kosten der Anträge, der Anlage und aller Arbeiten übernehmen
- Mieteinnahmen generieren!
Einzige Voraussetzung:
Dachfläche mit mind. 1.500qm
Worauf warten Sie?
Nehmen Sie jetzt Kontakt auf für eine entsprechende Machbarkeitsprüfung. Natürlich ist auch das Kostenlos.
veltrano GmbH
Fennstraße 47b
48155 Münster
T: +49 176 528 914 03
E: info@veltrano-beispiel.de

```html
<!DOCTYPE html>
<html lang="de">
<head>
<meta charset="utf-8">
<title>veltrano – Flyer Solarenergie</title>
<link href="https://fonts.googleapis.com/css2?family=Raleway:wght@300;400;500;600;700&display=swap" rel="stylesheet">
<style>
  :root {
    --green: #afcb08;
    --ink: #333333;
    --band: #f2f2f2;
    --white: #ffffff;
  }
  * { margin: 0; padding: 0; box-sizing: border-box; }
  html, body { width: 848px; height: 1200px; overflow: hidden; background: var(--white); }
  body { font-family: 'Raleway', sans-serif; color: var(--ink); }
  .flyer { position: relative; width: 848px; height: 1200px; overflow: hidden; background: var(--white); }

  .side-bar { position: absolute; left: 819px; top: 0; width: 29px; height: 564px; background: var(--green); }
  .band { position: absolute; left: 0; top: 564px; width: 848px; height: 264px; background: var(--band); }
  .foot-bar { position: absolute; left: 0; top: 1171px; width: 410px; height: 29px; background: var(--green); }

  .brand { position: absolute; left: 47px; top: 36px; }
  .brand-name { font-size: 52px; font-weight: 400; letter-spacing: -0.5px; line-height: 1; color: var(--ink); }
  .brand-tag { font-size: 12px; font-weight: 500; letter-spacing: 6.2px; margin-top: 10px; color: var(--ink); }

  .contact { position: absolute; left: 549px; top: 48px; padding-left: 16px; border-left: 1.5px solid var(--green); font-size: 13.5px; line-height: 17px; font-weight: 400; }
  .contact .company { color: var(--green); font-weight: 600; }

  .photo-frame { position: absolute; left: 75px; top: 173px; width: 444px; height: 418px; border: 1.5px solid var(--green); }
  .photo { position: absolute; left: 49px; top: 147px; width: 443px; height: 417px;
    background: linear-gradient(180deg, #e4e1d4 0%, #d9d2b6 30%, #8b8d72 52%, #4c5533 68%, #3b4658 82%, #2c3444 100%); }

  .eyebrow { position: absolute; display: flex; align-items: center; gap: 12px; font-size: 11px; font-weight: 600; letter-spacing: 1px; color: var(--green); }
  .eyebrow::before { content: ""; width: 30px; height: 1.5px; background: var(--green); }
  .eyebrow-profit { left: 549px; top: 268px; }
  .eyebrow-company { left: 75px; top: 621px; }

  .headline { position: absolute; left: 551px; top: 298px; width: 260px; font-size: 27px; line-height: 31px; font-weight: 500; }

  .company-title { position: absolute; left: 75px; top: 652px; font-size: 25px; font-weight: 600; }
  .company-text { position: absolute; left: 75px; top: 698px; width: 430px; font-size: 14px; line-height: 17px; font-weight: 400; }

  .requirement { position: absolute; left: 634px; top: 696px; width: 166px; height: 166px; border-radius: 50% 0 50% 50%; background: var(--green); color: var(--white); text-align: center; padding-top: 34px; font-size: 13px; line-height: 17px; }
  .requirement .lead { font-weight: 300; }
  .requirement .value { font-weight: 700; margin-top: 7px; }

  .benefits-title { position: absolute; left: 75px; top: 857px; font-size: 24px; font-weight: 500; }
  .benefit { position: absolute; display: flex; align-items: center; gap: 18px; font-size: 14px; line-height: 17px; font-weight: 400; }
  .benefit-icon { flex: none; width: 40px; height: 40px; border: 1.5px solid var(--green); border-radius: 50% 0 50% 50%; display: flex; align-items: center; justify-content: center; }
  .benefit-icon svg { width: 22px; height: 22px; fill: none; stroke: var(--green); stroke-width: 1.4; stroke-linecap: round; stroke-linejoin: round; }

  .cta { position: absolute; left: 75px; top: 1105px; font-size: 13.5px; line-height: 17px; }
  .cta-title { color: var(--green); font-weight: 600; }
</style>
</head>
<body>
<div class="flyer">
  <div class="side-bar"></div>
  <div class="band"></div>
  <div class="foot-bar"></div>

  <div class="brand">
    <div class="brand-name">veltrano</div>
    <div class="brand-tag">ENERGIETECHNIK</div>
  </div>

  <address class="contact" style="font-style:normal">
    <div class="company">veltrano GmbH</div>
    <div>Fennstraße 47b, 48155 Münster</div>
    <div>T: +49 176 528 914 03</div>
    <div>E: info@veltrano-beispiel.de</div>
  </address>

  <div class="photo-frame"></div>
  <div class="photo" role="img" aria-label="Monteur mit Schutzhelm setzt bei Sonnenuntergang ein Solarmodul auf ein Ziegeldach vor einer Hügellandschaft"></div>

  <div class="eyebrow eyebrow-profit">RENTABILITÄT</div>
  <h1 class="headline">Erwirtschaften auch Sie mit Ihrem Dach nun bares Geld!</h1>

  <div class="eyebrow eyebrow-company">VELTRANO</div>
  <h2 class="company-title">Pionier der grünen Energietechnik</h2>
  <p class="company-text">Veltrano ist Experte für grüne Energietechnik mit über 20 Jahren Erfahrung. Mit über 1.000 zufriedenen Kunden im Bereich Photo&shy;voltaikanlagen können wir auf einen großen Erfahrungsschatz zurückgreifen. Wenn wir am Werk sind, wird nicht nur das Klima geschont, sondern auch Sie als Kunde profitieren. Mit uns wird nachhaltiges Handeln kinderleicht und gleichzeitig rentabel.</p>

  <div class="requirement">
    <div class="lead">Einzige<br>Voraussetzung:</div>
    <div class="value">Dachfläche mit<br>mind. 1.500qm</div>
  </div>

  <h2 class="benefits-title">Ihre Vorteile</h2>

  <div class="benefit" style="left:75px; top:916px;">
    <span class="benefit-icon"><svg viewBox="0 0 24 24"><path d="M3 16h4l4 2h6l4-3"/><path d="M3 20h5l4 1h5"/><path d="M12 14V7"/><path d="M12 9c-3 0-5-2-5-5 3 0 5 2 5 5z"/><path d="M12 8c0-3 2-5 5-5 0 3-2 5-5 5z"/></svg></span>
    <span>Umwelt schonen durch das<br>Produzieren von grünem Strom</span>
  </div>
  <div class="benefit" style="left:75px; top:973px;">
    <span class="benefit-icon"><svg viewBox="0 0 24 24"><path d="M6 18a4 4 0 0 1 0-8 6 6 0 0 1 11.5 1.5A3.3 3.3 0 0 1 18 18z"/></svg></span>
    <span>Dach schützen vor Emissionen</span>
  </div>
  <div class="benefit" style="left:75px; top:1030px;">
    <span class="benefit-icon"><svg viewBox="0 0 24 24"><path d="M3 12l9-8 9 8"/><path d="M5 10v10h14V10"/><path d="M10 20v-6h4v6"/></svg></span>
    <span>Dachsanierungen anstatt von<br>Mietzahlungen möglich</span>
  </div>
  <div class="benefit" style="left:382px; top:916px;">
    <span class="benefit-icon"><svg viewBox="0 0 24 24"><ellipse cx="15" cy="5" rx="5" ry="2"/><path d="M10 5v10c0 1.1 2.2 2 5 2s5-.9 5-2V5"/><path d="M10 9c0 1.1 2.2 2 5 2s5-.9 5-2"/><path d="M10 13c0 1.1 2.2 2 5 2s5-.9 5-2"/><circle cx="8" cy="16" r="5"/></svg></span>
    <span>Keine Kosten, da wir alle Kosten<br>der Anträge, der Anlage und<br>aller Arbeiten übernehmen</span>
  </div>
  <div class="benefit" style="left:382px; top:973px;">
    <span class="benefit-icon"><svg viewBox="0 0 24 24"><rect x="3" y="14" width="4" height="7"/><rect x="10" y="11" width="4" height="10"/><rect x="17" y="8" width="4" height="13"/><path d="M4 10l6-4 3 2 6-5"/><path d="M16 3h3v3"/></svg></span>
    <span>Mieteinnahmen generieren!</span>
  </div>

  <div class="cta">
    <div class="cta-title">Worauf warten Sie?</div>
    <div>Nehmen Sie jetzt Kontakt auf für eine entsprechende Machbarkeitsprüfung. Natürlich ist auch das kostenlos.</div>
  </div>
</div>
</body>
</html>
```